Labour Day banner showcasing 20% off site

Banner graphic promoting our Labour Day sale
Size: 2000px x 600px
- examples from other companies and their sale banners have been uploaded for inspiration. Labour day examples are for the United States's holiday and submissions should NOT be in their country colours.
- product images can be found at www.tallpinegreens.com

Target Market(s)

19+

Industry/Entity Type

Cannabis

Requirements
Must have
• Phrases:
- “Happy Labour Day”
- “20% off site wide sale*"
- "Coupon code: Harvest20"
- Underneath phrase the date of sale “September 3rd - 7th”
- In tiny print “*excludes all sale and bundled items”
- MUST BE 2000px x 600px
Nice to have
• - images of the products or bud we carry which can be found at www.tallpinegreens.com
- bold
Should not have
• - company logo
- the American flag, we are a Canadian company, colours and flag should all be Canadian

```html
<!DOCTYPE html>
<html lang="en">
<head>
<meta charset="utf-8">
<title>Labour Day Sale Banner</title>
<link href="https://fonts.googleapis.com/css2?family=Poppins:wght@500;600;700;800&display=swap" rel="stylesheet">
<style>
  :root {
    --page: #ffffff;
    --sky-light: #5fa0d8;
    --sky: #2f7cc2;
    --sky-deep: #1f66ad;
    --red: #e1141c;
    --yellow: #f5dc35;
    --star: #f7d23a;
    --white: #ffffff;
    --ink: #333333;
  }
  html, body {
    margin: 0;
    width: 1200px;
    height: 1000px;
    overflow: hidden;
    background: var(--page);
    font-family: "Poppins", sans-serif;
  }
  .banner {
    position: absolute;
    left: 32px;
    top: 330px;
    width: 1136px;
    height: 340px;
    overflow: hidden;
    background: radial-gradient(ellipse at 55% 45%, var(--sky-light) 0%, var(--sky) 45%, var(--sky-deep) 100%);
  }
  .art { position: absolute; }
  .flag-art {
    left: 112px; top: 30px; width: 185px; height: 120px;
    transform: rotate(-22deg);
    border-radius: 10px;
    background: linear-gradient(90deg, var(--red) 0 26%, var(--white) 26% 74%, var(--red) 74% 100%);
  }
  .bud-art {
    left: 473px; top: 30px; width: 60px; height: 60px; border-radius: 50%;
    background: radial-gradient(circle, #9a8f45, #6b6a32);
  }
  .bottles-art {
    left: 22px; top: 185px; width: 135px; height: 150px; border-radius: 10px 10px 4px 4px;
    background: linear-gradient(180deg, #2a2a2a, #4a4a3c 55%, #c9b99a);
  }
  .bucket-art {
    left: 912px; top: 165px; width: 230px; height: 180px; border-radius: 50% 40% 0 0;
    background: linear-gradient(180deg, #5c5a3a 0 45%, #e3262d 45% 100%);
  }
  .ribbon {
    position: absolute;
    display: flex; align-items: center; justify-content: center;
    white-space: nowrap;
  }
  .ribbon-date {
    left: 523px; top: 36px; width: 395px; height: 58px;
    background: var(--yellow);
    transform: rotate(-4deg);
    color: var(--ink); font-weight: 600; font-size: 31px;
  }
  .ribbon-title {
    left: 215px; top: 92px; width: 735px; height: 100px;
    background: var(--red);
    transform: rotate(-5deg);
    color: var(--white); font-weight: 800; font-size: 70px; letter-spacing: 0.5px;
    gap: 22px;
  }
  .star { width: 20px; height: 20px; fill: var(--star); }
  .ribbon-offer {
    left: 316px; top: 178px; width: 512px; height: 74px;
    background: var(--white);
    transform: rotate(-4deg);
    font-size: 39px; gap: 14px;
  }
  .offer-amount { color: var(--red); font-weight: 800; font-size: 36px; }
  .offer-label { color: var(--ink); font-weight: 600; }
  .coupon {
    position: absolute; left: 250px; top: 298px;
    padding: 1px 12px;
    border: 2px solid var(--white);
    color: var(--white); font-size: 19px; font-weight: 500;
  }
  .footnote {
    position: absolute; left: 568px; top: 304px;
    color: var(--white); font-size: 18px; font-weight: 500;
  }
</style>
</head>
<body>
  <section class="banner">
    <div class="art flag-art" role="img" aria-label="Waving Canadian flag"></div>
    <div class="art bud-art" role="img" aria-label="Cannabis bud"></div>
    <div class="art bottles-art" role="img" aria-label="Three cannabis oil dropper bottles"></div>
    <div class="art bucket-art" role="img" aria-label="Striped popcorn bucket overflowing with cannabis buds"></div>

    <div class="ribbon ribbon-date">September 3rd - 7th</div>
    <div class="ribbon ribbon-title">
      <svg class="star" viewBox="0 0 20 20"><polygon points="10,1 12.6,7.2 19.5,7.6 14.2,12 15.9,18.8 10,15 4.1,18.8 5.8,12 0.5,7.6 7.4,7.2"/></svg>
      <span>HAPPY LABOUR DAY</span>
      <svg class="star" viewBox="0 0 20 20"><polygon points="10,1 12.6,7.2 19.5,7.6 14.2,12 15.9,18.8 10,15 4.1,18.8 5.8,12 0.5,7.6 7.4,7.2"/></svg>
    </div>
    <div class="ribbon ribbon-offer">
      <span class="offer-amount">20% OFF</span>
      <span class="offer-label">site wide sale</span>
    </div>

    <div class="coupon">Coupon code: Harvest20</div>
    <div class="footnote">*excludes all sale and bundled items</div>
  </section>
</body>
</html>
```